Marlbrook Crest Healthcare Needs a Business Card Design

We need a business card design for a company based in Shorewood IL called "Marlbrook Crest Healthcare". We provide an integrated medical model involving chiropractic, trigger point injections and other medical services in one location. I have attached our logo to this with the colors being in the puzzle design of the logo. We are looking for a great design that will WOW those around us but also be able to communicate our information easily

Industry/Entity Type

Medical

Contact Information for Business Card

This is a integrated Medical office featuring numerous services to clients in the office.

Requirements
Must have
• Logo

```html
<!DOCTYPE html>
<html lang="en">
<head>
<meta charset="utf-8">
<title>Marlbrook Crest Healthcare — Business Card</title>
<link href="https://fonts.googleapis.com/css2?family=Lato:wght@400;700&family=Sorts+Mill+Goudy&display=swap" rel="stylesheet">
<style>
  :root {
    --backdrop: #1c1c1c;
    --card: #ffffff;
    --orange: #f28b2c;
    --blue: #3b7cc2;
    --green: #5aa83c;
  }
  * { margin: 0; padding: 0; box-sizing: border-box; }
  html, body {
    width: 1200px;
    height: 900px;
    overflow: hidden;
    background: var(--backdrop);
  }
  .business-card {
    position: absolute;
    left: 110px;
    top: 172px;
    width: 980px;
    height: 556px;
    background: var(--card);
    box-shadow: 0 18px 40px rgba(0,0,0,0.5);
  }
  .brand {
    position: absolute;
    left: 290px;
    top: 128px;
    display: flex;
    align-items: center;
    gap: 14px;
  }
  .brand-square {
    width: 58px;
    height: 58px;
    background: var(--blue);
  }
  .brand-name {
    font-family: "Sorts Mill Goudy", Georgia, serif;
    font-size: 40px;
    line-height: 1;
    color: var(--blue);
    text-transform: uppercase;
    letter-spacing: 0.5px;
  }
  .tagline {
    position: absolute;
    left: 160px;
    top: 232px;
    font-family: "Sorts Mill Goudy", Georgia, serif;
    font-size: 23px;
    color: var(--green);
  }
  .person {
    position: absolute;
    left: 150px;
    top: 386px;
    color: var(--orange);
    font-family: "Lato", Arial, sans-serif;
  }
  .person-name { font-size: 31px; font-weight: 400; line-height: 1.1; }
  .person-role { font-size: 19px; margin-top: 2px; }
  .contacts {
    position: absolute;
    left: 620px;
    top: 300px;
    list-style: none;
    font-family: "Lato", Arial, sans-serif;
    font-size: 18px;
    color: var(--orange);
  }
  .contacts li {
    display: flex;
    align-items: center;
    gap: 14px;
    height: 30px;
  }
  .contacts svg { width: 20px; height: 20px; fill: var(--blue); flex: none; }
</style>
</head>
<body>
  <div class="business-card">
    <div class="brand">
      <div class="brand-square"></div>
      <div class="brand-name">Marlbrook Crest Healthcare</div>
    </div>

    <p class="tagline">Chiropractic, Trigger point injections and Other medical services</p>

    <div class="person">
      <div class="person-name">Name Title</div>
      <div class="person-role">Designation</div>
    </div>

    <ul class="contacts">
      <li>
        <svg viewBox="0 0 20 20" aria-hidden="true"><path d="M2 7c0-2 3-4 8-4s8 2 8 4v2h-4V7H6v2H2zM5 10h10l2 7H3z"/></svg>
        <span>0123 456789</span>
      </li>
      <li>
        <svg viewBox="0 0 20 20" aria-hidden="true"><path d="M1 4h18v12H1zM2.5 5.5 10 11l7.5-5.5z" fill-rule="evenodd"/></svg>
        <span>info@companyname.com</span>
      </li>
      <li>
        <svg viewBox="0 0 20 20" aria-hidden="true"><path d="M8 12 12 8M7 10l-3 3a2.5 2.5 0 0 0 3.5 3.5l3-3M13 10l3-3a2.5 2.5 0 0 0-3.5-3.5l-3 3" fill="none" stroke="#3b7cc2" stroke-width="2" stroke-linecap="round"/></svg>
        <span>www.companyname.com</span>
      </li>
    </ul>
  </div>
</body>
</html>
```